Brightmere Business Card Redesign & Logo Update

We need to update our business cards to something more modern and fresh. Brightmere can provide the current color schemes and old design examples, but welcome creativity in helping us with this redesign. PLEASE NOTE that we no longer utilize the "tree" and/or "leaf" imagery in our branding. If able would apprecaite an update on the quality of our "words only" logo in Ai. / PNG formats too.

Target Market(s)

Investors, landowners, corporate partners, contractors

Industry/Entity Type

Environmental Restoration & Conservation

Contact Information for Business Card

Logo, persons name, title, mailing address, phone and email, website url

Font styles to use
Other font styles liked:
• Merriweather

Requirements
Nice to have
• Logo, persons name, title, mailing address, phone and email, website url, but open to ideams
Should not have
• No all back backgrounds

```html
<!DOCTYPE html>
<html lang="en">
<head>
<meta charset="utf-8">
<title>Brightmere Business Card</title>
<link rel="stylesheet" href="https://fonts.googleapis.com/css2?family=Oswald:wght@500;700&family=Lato:wght@400;700&display=swap">
<style>
  :root {
    --forest: #137c36;
    --forest-deep: #0f6a2d;
    --amber: #ee7d0b;
    --paper: #ffffff;
    --ink: #1a1a1a;
    --backdrop: #e9eaeb;
  }
  * { box-sizing: border-box; margin: 0; padding: 0; }
  html, body { width: 1200px; height: 875px; overflow: hidden; }
  body { background: var(--backdrop); position: relative; font-family: "Lato", sans-serif; }

  .card {
    position: absolute;
    width: 620px;
    height: 354px;
    border-radius: 22px;
    overflow: hidden;
    box-shadow: 0 10px 30px rgba(0,0,0,0.18);
  }

  /* Front: person & contact details */
  .card-front { left: 170px; top: 48px; background: var(--forest); color: var(--paper); }
  .identity {
    position: absolute; left: 0; top: 0; width: 340px; height: 100%;
    display: flex; flex-direction: column; justify-content: center; align-items: flex-end;
    padding-right: 32px;
  }
  .person-name {
    font-family: "Oswald", sans-serif; font-weight: 700;
    font-size: 44px; letter-spacing: 0.5px; line-height: 1; text-transform: uppercase;
  }
  .person-title { font-size: 19px; margin-top: 6px; }
  .divider {
    position: absolute; left: 340px; top: 92px; width: 1.5px; height: 170px; background: var(--paper);
  }
  .contact-list {
    position: absolute; left: 366px; top: 82px; list-style: none; font-size: 15px; line-height: 1.25;
  }
  .contact-list li { display: flex; align-items: flex-start; gap: 10px; margin-bottom: 6px; }
  .contact-list svg { width: 14px; height: 14px; flex: none; margin-top: 2px; fill: var(--paper); }

  /* Back: wordmark */
  .card-back { left: 410px; top: 470px; background: var(--paper); }
  .wordmark {
    position: absolute; left: 0; right: 0; top: 130px; text-align: center;
    font-family: "Oswald", sans-serif; font-weight: 700; font-size: 74px;
    letter-spacing: 2px; text-transform: uppercase; color: var(--forest); line-height: 1;
  }
  .band-amber { position: absolute; left: 0; bottom: 0; width: 58%; height: 12px; background: var(--amber); }
  .band-forest { position: absolute; left: 58%; right: 0; bottom: 8px; height: 12px; background: var(--forest); }
</style>
</head>
<body>
  <section class="card card-front">
    <div class="identity">
      <h1 class="person-name">Daniel Harper</h1>
      <p class="person-title">Founder &amp; CEO</p>
    </div>
    <div class="divider"></div>
    <ul class="contact-list">
      <li>
        <svg viewBox="0 0 14 14"><path d="M7 0a5 5 0 0 0-5 5c0 3.6 5 9 5 9s5-5.4 5-9a5 5 0 0 0-5-5zm0 7a2 2 0 1 1 0-4 2 2 0 0 1 0 4z"/></svg>
        <span>48 Fernhill Road<br>Ashvale, State 20417</span>
      </li>
      <li>
        <svg viewBox="0 0 14 14"><path d="M3 0l2.5 3-1.5 2c.8 1.8 2.2 3.2 4 4l2-1.5 3 2.5-1.5 3C6 13 1 8 0 1.5z"/></svg>
        <span>(555) 314-2708</span>
      </li>
      <li>
        <svg viewBox="0 0 14 14"><path d="M4 0h6a1 1 0 0 1 1 1v12a1 1 0 0 1-1 1H4a1 1 0 0 1-1-1V1a1 1 0 0 1 1-1zm0 2v9h6V2z"/></svg>
        <span>(555) 314-2709</span>
      </li>
      <li>
        <svg viewBox="0 0 14 14"><path d="M3 0h8v4H3zM1 5h12v6h-2V9H3v2H1zm3 5h6v4H4z"/></svg>
        <span>(555) 314-2710</span>
      </li>
      <li>
        <svg viewBox="0 0 14 14"><path d="M0 3h14v1L7 8 0 4zm0 2.5l7 4 7-4V11H0z"/></svg>
        <span>hello@brightmere-eco.com</span>
      </li>
      <li>
        <svg viewBox="0 0 14 14"><path d="M7 0a7 7 0 1 0 0 14A7 7 0 0 0 7 0zm4.8 6H9.9a10 10 0 0 0-1-4.2A5 5 0 0 1 11.8 6zM7 2c.6.9 1 2.3 1 4H6c0-1.7.4-3.1 1-4zM2.2 8h1.9c.1 1.6.4 3 1 4.2A5 5 0 0 1 2.2 8zm1.9-2H2.2a5 5 0 0 1 2.9-4.2C4.5 3 4.2 4.4 4.1 6zM7 12c-.6-.9-1-2.3-1-4h2c0 1.7-.4 3.1-1 4zm1.9.2c.6-1.2.9-2.6 1-4.2h1.9a5 5 0 0 1-2.9 4.2z"/></svg>
        <span>www.brightmere-eco.com</span>
      </li>
    </ul>
  </section>

  <section class="card card-back">
    <div class="wordmark">Brightmere</div>
    <div class="band-amber"></div>
    <div class="band-forest"></div>
  </section>
</body>
</html>
```